Business Card Design for Brisley Consulting

I need business cards for a new company I have started called Brisley Consulting. Brisley Consulting is a new business based out of Columbus Ohio. I will be operating in Ohio as well as nationwide. Brisley Consulting is a professional organization designed to fit your organization's specific needs. We are dedicated to the success of organizations. We handle human resource management, leadership coaching and development, executive training, team building, personality inventories and searches, performance evaluations, temp. services, custom solutions and more. Brisley consulting services a variety of industries such as government agencies, educational systems, board of directors, construction services and more, please visit our website for a full list of services (the website will be important).

I leave the design to you. I am a 45 year old male. I was in the education field for 21 years and 11 years as a superintendent. I like the colors red and black. Don't know what works, I will leave that to you as well. I would like to have it be catchy yet masculine. I have been associated with many organizations over the years both public and private, and will be reaching out to the public and private sector.

I do need a logo...so I leave that to you as well. Company name is Brisley Consulting.

Industry/Entity Type

Construction

Contact Information for Business Card

Gordon T. Brisley, President
Brisley Consulting
47 W.Ninth St. Suite 385
Arcade at Kelmont Court
Columbus, Ohio 43287

Phone : 330-418-2973
email : gbrisley@brisleyadvise.com
web : www.brisleyadvise.com
twitter : @brisleyadvise
facebook : Brisley Consulting

```html
<!DOCTYPE html>
<html lang="en">
<head>
<meta charset="utf-8">
<title>Brisley Consulting – Business Card</title>
<link rel="stylesheet" href="https://fonts.googleapis.com/css2?family=Aldrich&display=swap">
<style>
  :root {
    --backdrop: #2c2c2e;
    --card: #fbfbfb;
    --accent: #c8161d;
    --ink: #141414;
    --icon-glyph: #ffffff;
  }
  * { box-sizing: border-box; margin: 0; padding: 0; }
  html, body {
    width: 1200px;
    height: 816px;
    overflow: hidden;
    background: var(--backdrop);
  }
  .card {
    position: absolute;
    left: 75px;
    top: 108px;
    width: 1050px;
    height: 600px;
    background: var(--card);
    border-radius: 44px;
    font-family: "Aldrich", sans-serif;
    color: var(--ink);
  }
  .rule {
    position: absolute;
    height: 6px;
    background: var(--accent);
  }
  .rule--top { left: 148px; top: 140px; width: 346px; }
  .rule--bottom { left: 72px; top: 262px; width: 422px; }
  .icon {
    position: absolute;
    width: 54px;
    height: 54px;
  }
  .identity__icon { left: 80px; top: 178px; }
  .identity__name {
    position: absolute;
    left: 152px;
    top: 166px;
    font-size: 27px;
    letter-spacing: 1px;
    white-space: nowrap;
  }
  .identity__role {
    position: absolute;
    left: 152px;
    top: 204px;
    font-size: 21px;
    letter-spacing: 1.5px;
  }
  .contact__icon--phone { left: 80px; top: 313px; }
  .contact__icon--web { left: 80px; top: 391px; }
  .contact__icon--place { left: 80px; top: 481px; }
  .contact__text {
    position: absolute;
    left: 152px;
    font-size: 20px;
    line-height: 28px;
    letter-spacing: 1px;
    white-space: nowrap;
  }
  .contact__text--phone { top: 312px; }
  .contact__text--web { top: 390px; }
  .contact__text--place { top: 466px; }
  .brand-name {
    position: absolute;
    right: 70px;
    top: 312px;
    font-size: 36px;
    letter-spacing: 4px;
    font-variant: small-caps;
    color: var(--accent);
    white-space: nowrap;
  }
</style>
</head>
<body>
  <main class="card">
    <div class="rule rule--top"></div>

    <svg class="icon identity__icon" viewBox="0 0 54 54" aria-hidden="true">
      <circle cx="27" cy="27" r="27" fill="var(--accent)"/>
      <circle cx="27" cy="21" r="8" fill="var(--icon-glyph)"/>
      <path d="M13 40c2-8 8-11 14-11s12 3 14 11z" fill="var(--icon-glyph)"/>
    </svg>
    <div class="identity__name">GORDON T. BRISLEY</div>
    <div class="identity__role">President</div>

    <div class="rule rule--bottom"></div>

    <svg class="icon contact__icon--phone" viewBox="0 0 54 54" aria-hidden="true">
      <circle cx="27" cy="27" r="27" fill="var(--accent)"/>
      <rect x="19" y="12" width="16" height="30" rx="3" fill="none" stroke="var(--icon-glyph)" stroke-width="3"/>
      <circle cx="27" cy="37" r="1.8" fill="var(--icon-glyph)"/>
    </svg>
    <div class="contact__text contact__text--phone">330-418-2973<br>@brisleyadvise</div>

    <svg class="icon contact__icon--web" viewBox="0 0 54 54" aria-hidden="true">
      <circle cx="27" cy="27" r="27" fill="var(--accent)"/>
      <rect x="13" y="15" width="28" height="19" rx="2" fill="none" stroke="var(--icon-glyph)" stroke-width="3"/>
      <path d="M21 40h12M27 34v6" stroke="var(--icon-glyph)" stroke-width="3"/>
    </svg>
    <div class="contact__text contact__text--web">gbrisley@brisleyadvise.com<br>www.brisleyadvise.com</div>

    <svg class="icon contact__icon--place" viewBox="0 0 54 54" aria-hidden="true">
      <circle cx="27" cy="27" r="27" fill="var(--accent)"/>
      <path d="M27 42c-6-8-10-13-10-18a10 10 0 0 1 20 0c0 5-4 10-10 18z" fill="var(--icon-glyph)"/>
      <circle cx="27" cy="24" r="4" fill="var(--accent)"/>
    </svg>
    <div class="contact__text contact__text--place">47 W.Ninth St. Suite 385<br>Arcade at Kelmont Court<br>Columbus, Ohio 43287</div>

    <div class="brand-name">Brisley Consulting</div>
  </main>
</body>
</html>
```